International Dental Education Website

This project is for a small teaching center on endodontic and micro dentistry in Norway. We need a Wordpress website design to display and highlight dental educational courses. Please use our new logo - see attached file. We like lighter, pastel oriented colors. The following sites are nicely laid out and you can use these as a guideline of sorts but I do want a unique site.
http://vorplex.example/en, http://www.toothmarlow.example/Education.aspx?currentSection=courses&cid=14,
http://www.pulpvesker.example/.
Please create a space for a possible video on the home page. Please include a small contact form on the home page(name, email, phone, text box). Would like a horizonatal naviagtion bar. Would like an image to go across the whole top part of the site and this may rotate. Please use a stock image that shows a classroom type setting. Put phone number at the top of the screen. Put address and sitemap in a footer.

Reason: Upcoming vacation with limited internet access. Please continue to submit any designs. Thanks you.

Reason: The client is from a foreign country and is on an extended vacation.

Target Market(s)

General dentists (GPs) and specialists in Endodontics

Industry/Entity Type

Dental

Requirements
Must have
• Sitemap: HOME, COURSES, LECTURER, CONTACT US,
NORWEGIAN/ENGLISH. Phone number is: +47 93516270. Business name and address: Kali Rom AS, Endodontic Teaching Center,
Fjeldstads vei 17C, 0371 Oslo, Norway.

```html
<!DOCTYPE html>
<html lang="en">
<head>
<meta charset="utf-8">
<title>Kali Rom – Endodontic Teaching Center</title>
<link rel="stylesheet" href="https://fonts.googleapis.com/css2?family=Cabin:wght@400;500&display=swap">
<style>
:root{
  --bg:#86d1d8;
  --page:#ffffff;
  --teal:#6cc5cc;
  --nav:#8ad3d9;
  --text:#333;
  --muted:#555;
  --grey-bar:#a3b3b8;
  --line:#d3dcdf;
  --panel:#e6ecee;
}
*{box-sizing:border-box;margin:0;padding:0}
html,body{width:1200px;height:999px;overflow:hidden}
body{background:var(--bg);font-family:"Cabin",sans-serif;color:var(--text);position:relative}
.top-rule,.bottom-rule{position:absolute;left:0;width:1200px;background:var(--grey-bar)}
.top-rule{top:9px;height:7px}
.bottom-rule{bottom:0;height:5px}

.page{position:absolute;left:153px;top:17px;width:894px;height:879px;background:var(--page);box-shadow:0 0 8px rgba(0,0,0,.2)}
.brand{position:absolute;left:36px;top:28px;font-size:36px;font-weight:500;line-height:44px;color:var(--teal)}

.phone{position:absolute;left:297px;top:17px;height:20px;font-size:12.5px;color:var(--muted);display:flex;align-items:center;gap:6px;white-space:nowrap}
.phone strong{color:var(--teal);font-size:16px;font-weight:500;margin-left:4px}
.search{position:absolute;left:520px;top:16px;width:212px;height:26px;border:1px solid #ccc;background:linear-gradient(#fff,#ececec);font-size:11.5px;color:#888;padding:6px 10px}
.search svg{position:absolute;right:8px;top:5px}
.lang{position:absolute;left:744px;top:18px;width:131px;height:22px;border:1px solid #ccc;font-size:9.5px;padding:5px 7px;color:#222}
.lang svg{position:absolute;right:8px;top:8px}

.nav{position:absolute;left:292px;top:57px;width:583px;height:29px;background:linear-gradient(#9adbe0,var(--nav));display:flex;box-shadow:0 2px 3px rgba(0,0,0,.15)}
.nav a{color:#222;text-decoration:none;font-size:11.5px;display:flex;align-items:center;justify-content:center;border-right:1px solid #fff;white-space:nowrap}
.nav a:last-child{border:none}

.hero{position:absolute;left:16px;top:106px;width:859px;height:337px;background:linear-gradient(120deg,#d9cfc8 0%,#e9e4df 40%,#d4dcd6 70%,#9bb8b0 100%);box-shadow:0 3px 6px rgba(0,0,0,.25)}
.dots{position:absolute;right:28px;bottom:13px;display:flex;gap:4px}
.dots i{width:11px;height:11px;border-radius:50%;background:#fff}
.dots i.on{background:#e0592c;box-shadow:0 0 0 2px #fff inset}

.quick{position:absolute;left:17px;top:463px;width:339px;height:216px;background:linear-gradient(#a5dee2,#73c3c9)}
.quick h2{position:absolute;left:16px;top:13px;width:303px;font-weight:400;font-size:18px;line-height:22px;padding-bottom:9px;border-bottom:1px solid #b6e0e3}
.field{position:absolute;left:22px;font-size:11.5px;line-height:14px}
.input{position:absolute;left:118px;width:200px;background:#fff;border:1px solid #dfe7e9}
.submit{position:absolute;left:252px;top:186px;width:66px;height:22px;background:linear-gradient(#7c878c,#555f64);color:#fff;font-size:11.5px;text-align:center;line-height:22px}

.welcome{position:absolute;left:369px;top:463px;width:511px;height:214px;border:1px solid var(--line)}
.welcome h3{position:absolute;left:20px;top:53px;font-weight:400;font-size:21px;line-height:26px;color:#888}
.welcome .brand{left:22px;top:92px;font-size:30px;line-height:38px}
.welcome p{position:absolute;left:157px;top:27px;width:329px;border-left:1px solid var(--line);padding-left:18px;font-size:10.6px;line-height:18.5px;text-align:justify;color:#555}

.card{position:absolute;top:689px;width:282px;height:176px;border:1px solid var(--line);background:linear-gradient(#fff 40%,var(--panel));box-shadow:0 2px 3px rgba(0,0,0,.15)}
.card h3{position:absolute;left:10px;top:13px;width:264px;font-weight:400;font-size:18px;line-height:22px;padding:0 0 7px 8px;border-bottom:1px solid var(--line)}
.thumb{position:absolute;left:17px;top:61px;width:92px;height:77px;background:linear-gradient(135deg,#7aa0bb,#d8dde3 55%,#f2efec);box-shadow:0 1px 3px rgba(0,0,0,.3)}
.card p{position:absolute;left:126px;top:59px;width:142px;font-size:11px;line-height:18.5px;text-align:justify}
.more{position:absolute;right:14px;top:145px;font-size:10.5px;line-height:12px;padding:4px 5px;border:1px solid #ccc;background:#fff;box-shadow:0 1px 2px rgba(0,0,0,.2)}

.footer-address{position:absolute;left:152px;top:921px;font-size:11.5px;line-height:19px}
.footer-nav{position:absolute;right:153px;top:921px;font-size:11.5px;line-height:19px;text-align:right;white-space:nowrap}
</style>
</head>
<body>
<div class="top-rule"></div>
<div class="page">
  <div class="brand">Kali Rom</div>
  <div class="phone">
    <svg width="15" height="12" viewBox="0 0 16 13"><path d="M1 4c3-3 11-3 14 0l-2 2-2-1V3H5v2L3 6z M4 7h8l2 5H2z" fill="#222"/></svg>
    Call Us Now <strong>+47 93516270</strong>
  </div>
  <div class="search">Search
    <svg width="13" height="13" viewBox="0 0 14 14"><circle cx="5" cy="5" r="3.5" stroke="#222" stroke-width="2" fill="none"/><path d="M8 8l5 5" stroke="#222" stroke-width="2.4"/></svg>
  </div>
  <div class="lang">Select Language<svg width="8" height="5"><path d="M0 0h8L4 5z" fill="#222"/></svg></div>
  <nav class="nav">
    <a style="width:113px">HOME</a><a style="width:109px">COURSES</a><a style="width:110px">LECTURER</a><a style="width:117px">CONTACT US</a><a style="width:134px">NORWEGIAN / ENGLISH</a>
  </nav>
  <div class="hero" role="img" aria-label="Rotating banner photo: dentist treating a patient">
    <div class="dots"><i></i><i></i><i class="on"></i><i></i><i></i><i></i></div>
  </div>
  <section class="quick">
    <h2>Quick Contact</h2>
    <span class="field" style="top:62px">Name</span><div class="input" style="top:60px;height:23px"></div>
    <span class="field" style="top:98px">E mail</span><div class="input" style="top:93px;height:23px"></div>
    <span class="field" style="top:141px;left:25px">Message</span><div class="input" style="top:126px;height:52px"></div>
    <div class="submit">Submit</div>
  </section>
  <section class="welcome">
    <h3>Welcome to</h3>
    <div class="brand">Kali Rom</div>
    <p>Lorem Ipsum is simply dummy text of the printing and typesetting industry. Lorem Ipsum has been the industry's standard dummy text ever since the 1500s, when an unknown printer took a galley of type and scrambled it to make a type specimen book. It has survived not only five centuries, but also the leap into electronic typesetting, remaining essentially unchanged. It was popularised in the 1960s with the release of Letraset sheets containing Lorem Ipsum passages, and more recently with desktop publishing....</p>
  </section>
  <section class="card" style="left:18px"><h3>Courses</h3><div class="thumb" role="img" aria-label="Photo of a dental treatment"></div><p>Lorem Ipsum is simply dummy text of the printing and typesetting industry. Lorem Ipsum has....</p><span class="more">Read More</span></section>
  <section class="card" style="left:307px"><h3>Lecturer</h3><div class="thumb" role="img" aria-label="Photo of a lecturer treating a patient"></div><p>Lorem Ipsum is simply dummy text of the printing and typesetting industry. Lorem Ipsum has....</p><span class="more">Read More</span></section>
  <section class="card" style="left:597px"><h3>Services</h3><div class="thumb" role="img" aria-label="Photo of a dental treatment"></div><p>Lorem Ipsum is simply dummy text of the printing and typesetting industry. Lorem Ipsum has....</p><span class="more">Read More</span></section>
</div>
<footer>
  <div class="footer-address">Kali Rom AS, Endodontic Teaching Center,<br>Fjeldstads vei 17C, 0371 Oslo, Norway</div>
  <div class="footer-nav">HOME &nbsp;| &nbsp;COURSES &nbsp;| &nbsp;LECTURER &nbsp;| &nbsp;CONTACT US &nbsp;| &nbsp;NORWEGIAN/ENGLISH &nbsp;| &nbsp;SITE MAP<br>Copyrights @ 2012 All Rights Reserved</div>
</footer>
<div class="bottom-rule"></div>
</body>
</html>
```